Newspaper Ad for Front page strip

Corvel Quick Lending is a micro lender operating in the Caribbean. This ad is for our Trinidad and Tobago location.
Would like to design a catchy banner ad for the front page of a daily newspaper. The ad should capture 1) that we offer unsecured loans up to $40,000. 2) customer can apply online or over the phone 3) that the process is quick.
We have included the a snapshot of our Instagram posts as well as the newspaper location and size of the ad.
We have booked this ad spot for the year so the more engaging we can make it the better. Maybe we can do a series of ads or weekly storyline . Let’s be creative.
https://www.instagram.com/corvelquicklending/
www.corvelquick lending.example
Target Market(s)
Mass population.
Industry/Entity Type
Banking
Look and feel

```html
<!DOCTYPE html>
<html lang="en">
<head>
<meta charset="utf-8">
<title>Corvel Quick Lending – Front Page Strip</title>
<link rel="stylesheet" href="https://fonts.googleapis.com/css2?family=Bebas+Neue&family=Montserrat:wght@600;700;800&display=swap">
<style>
  :root{
    --backdrop:#d9d9d9;
    --paper:#ffffff;
    --brand-red:#d7101e;
    --brand-blue:#0a5eab;
    --brand-green:#0f8c3e;
    --gold:#f7c56b;
    --ink-white:#ffffff;
  }
  *{box-sizing:border-box;margin:0;padding:0}
  html,body{width:1200px;height:1200px;overflow:hidden;background:var(--backdrop)}
  .strip-frame{position:absolute;left:472px;top:40px;width:255px;height:1120px}
  .strip{position:absolute;left:0;top:0;width:390px;height:1715px;background:var(--paper);
    transform:scale(0.653);transform-origin:0 0;overflow:hidden}
  .display{font-family:"Bebas Neue",Impact,sans-serif;line-height:1;color:var(--ink-white);text-align:center;position:absolute;left:0;width:100%}
  .kicker{font-family:"Montserrat",Arial,sans-serif;font-weight:800;color:var(--ink-white);text-align:center;position:absolute;left:0;width:100%;letter-spacing:1px;line-height:1}

  .brand{position:absolute;top:34px;left:0;width:100%;display:flex;justify-content:center;align-items:center;gap:8px}
  .brand-mark{width:16px;height:16px;background:var(--brand-red)}
  .brand-name{font-family:"Montserrat",Arial,sans-serif;font-weight:800;font-size:22px;color:var(--brand-red)}

  .panel{position:absolute;left:11px;width:369px;overflow:visible}
  .panel-loans{top:95px;height:513px;background:var(--brand-red)}
  .panel-apply{top:614px;height:514px;background:var(--brand-blue)}
  .footer-band{position:absolute;left:0;top:1545px;width:390px;height:170px;background:var(--brand-red)}
  .panel-quick{top:1131px;left:6px;width:378px;height:522px;background:var(--brand-green);border:4px solid var(--paper)}

  .photo{position:absolute}
  .photo-loans{left:44px;top:210px;width:260px;height:303px;border-radius:120px 120px 0 0;
    background:linear-gradient(180deg,#a8131c 0%,#c79a2a 55%,#e0c22a 100%)}
  .photo-apply{left:59px;top:176px;width:225px;height:338px;border-radius:100px 100px 0 0;
    background:linear-gradient(180deg,#3a4a66 0%,#8a8a8a 40%,#f0cf5c 70%,#c9824e 100%)}
  .photo-quick{left:86px;top:355px;width:196px;height:159px;border-radius:90px 90px 0 0;
    background:linear-gradient(180deg,#5a3a22 0%,#d8b42a 60%,#e6c62c 100%)}

  .pointer{position:absolute;width:22px;height:12px}

  .phone-band{position:absolute;left:26px;top:144px;width:320px;height:26px;background:var(--brand-green);
    font-family:"Montserrat",Arial,sans-serif;font-weight:800;font-size:21px;color:var(--ink-white);
    text-align:center;line-height:27px;letter-spacing:1px}

  .site-url{position:absolute;left:0;top:1673px;width:100%;text-align:center;font-family:"Montserrat",Arial,sans-serif;
    font-weight:700;font-size:14px;letter-spacing:1.6px;color:var(--ink-white)}
</style>
</head>
<body>
  <div class="strip-frame">
    <div class="strip">
      <header class="brand">
        <span class="brand-mark"></span>
        <span class="brand-name">Corvel Quick Lending</span>
      </header>

      <section class="panel panel-loans">
        <p class="kicker" style="top:34px;font-size:20px">WE OFFER</p>
        <h1 class="display" style="top:58px;font-size:58px">UNSECURED LOANS</h1>
        <p class="kicker" style="top:118px;font-size:14px;letter-spacing:.5px">Up to</p>
        <p class="display" style="top:134px;font-size:66px;color:var(--gold)">$40,000</p>
        <div class="photo photo-loans" role="img" aria-label="Excited woman in a yellow sweater holding a fan of cash"></div>
        <svg class="pointer" style="right:6px;bottom:-12px" viewBox="0 0 22 12" aria-hidden="true"><polygon points="0,0 22,0 11,12" fill="var(--brand-red)"/></svg>
      </section>

      <section class="panel panel-apply">
        <p class="kicker" style="top:53px;font-size:20px">CUSTOMER CAN</p>
        <h2 class="display" style="top:78px;font-size:70px">APPLY ONLINE</h2>
        <p class="phone-band">OR OVER THE PHONE</p>
        <div class="photo photo-apply" role="img" aria-label="Smiling woman sitting cross-legged with a yellow laptop"></div>
        <svg class="pointer" style="left:6px;bottom:-12px" viewBox="0 0 22 12" aria-hidden="true"><polygon points="0,0 22,0 11,12" fill="var(--brand-blue)"/></svg>
      </section>

      <div class="footer-band"></div>

      <section class="panel panel-quick">
        <p class="kicker" style="top:28px;font-size:34px">THAT THE</p>
        <h2 class="display" style="top:66px;font-size:104px">PROCESS</h2>
        <p class="kicker" style="top:166px;font-size:34px">IS</p>
        <h2 class="display" style="top:201px;font-size:150px">QUICK</h2>
        <div class="photo photo-quick" role="img" aria-label="Surprised woman in a yellow sweater pointing at her phone"></div>
      </section>

      <p class="site-url">www.corvelquicklending.example</p>
    </div>
  </div>
</body>
</html>
```